Modern Yoga Studio Timetable and Flyer Design

We have a comprehensive class timetable and we are wanting to a clean modern look for our Spring timetable.

We require a double sided flyer with our class timetable included.
We would prefer an A5 size (postcard) or DL (1/3 A4).

We would like the final flyer to have.
Side A : Yoga image, logo

Cedar Pose Loft
address: 3/17 Weltmore Street, Parvindale
website: cedarpose.com.au
mobile: 0471 592 640

Side B: Clear easy to read timetable with a break down of class types and website.

We would also like to have a copy of the timetable itself as a separate jpg or pdf for use on our website to download.

Thank you.
Yours kindly,
Hilde

I have attached a sample of another timetable of which I like the look and feel of, however this is just a guide. I've also attached our 'new' schedule in WORD plus uploaded our last design of the front.

Target Market(s)

Women aged 30-45

Industry/Entity Type

Health And Wellness

Font styles to use
Other font styles liked:
• Brandon Grotesque, Jenna Sue

Colors
6c459b
33a6d7
ffffff

Requirements
Must have
• A definitive colour to decipher between different class types on our timetable. Where each colour represents a different class type. Colours and layouts similar to our website design, see www.cedarpose.com.au
Nice to have
• I've included a design of another studio whose timetable design I like. One of our own yoga images instead of a stock image.
Should not have
• No dark gridlines between the cells/boxes in the timetables. Please don't use stock yoga images.

```html
<!DOCTYPE html>
<html lang="en">
<head>
<meta charset="utf-8">
<title>Cedar Pose Loft – Flyer</title>
<link href="https://fonts.googleapis.com/css2?family=Lobster&family=Lato:wght@300;400;700;900&family=Oswald:wght@500&display=swap" rel="stylesheet">
<style>
  :root{
    --purple:#6c459b;
    --purple-deep:#3f2a66;
    --blue:#33a6d7;
    --blue-bright:#1e8fe0;
    --blue-cell:#b3e3f7;
    --pink:#f6b6d9;
    --pink-edge:#f3a6d0;
    --ink:#2a2a35;
    --paper:#ffffff;
    --paper-grey:#ececec;
    --stage:#e6e6e6;
  }
  *{box-sizing:border-box;margin:0;padding:0}
  html,body{width:1200px;height:1200px;overflow:hidden;background:var(--stage)}
  .canvas{position:relative;width:1200px;height:1200px}
  .card{position:absolute;left:230px;width:740px;height:522px;background:linear-gradient(180deg,#f7f7f7,var(--paper-grey));overflow:hidden}
  .card--front{top:60px}
  .card--back{top:620px}
  .card svg.art{position:absolute;inset:0}
  .band{position:absolute;left:0;right:0;bottom:0;height:30px;background:linear-gradient(90deg,var(--purple-deep),var(--purple) 50%,var(--purple-deep))}

  .wordmark{position:absolute;left:32px;top:62px;font:300 26px/1 'Lato',sans-serif;letter-spacing:9px;color:var(--blue)}
  .contact{position:absolute;left:26px;top:408px;list-style:none;font:400 17px/22.5px 'Lato',sans-serif;color:var(--ink)}
  .contact li{display:flex;align-items:center;gap:8px}
  .contact svg{width:13px;height:13px;flex:none}
  .studio-name{position:absolute;right:24px;top:378px;text-align:right;color:var(--paper);font-family:'Lobster',cursive}
  .studio-name .main{display:block;font-size:60px;line-height:1}
  .studio-name .sub{display:block;font-size:38px;line-height:1.05}

  .tt-title{position:absolute;left:0;right:0;top:18px;text-align:center;font:400 23px/1 'Lobster',cursive;color:var(--purple)}
  .tt-frame{position:absolute;left:30px;top:58px;width:690px;border:4px solid var(--pink-edge);border-radius:24px;overflow:hidden;background:var(--paper)}
  .tt-inner{border:2px solid var(--blue-bright);border-radius:20px;overflow:hidden}
  table.timetable{width:100%;border-collapse:collapse;table-layout:fixed;font:500 10px/1 'Oswald',sans-serif;color:var(--ink)}
  .timetable th,.timetable td{border:2px solid var(--blue-bright);padding:0 6px;text-align:left;height:26.3px;vertical-align:middle}
  .timetable tr:first-child th{border-top:none}
  .timetable tr:last-child td{border-bottom:none}
  .timetable th:first-child,.timetable td:first-child{border-left:none}
  .timetable th:last-child,.timetable td:last-child{border-right:none}
  .timetable thead th{background:var(--pink);font:700 11px/1 'Lato',sans-serif;height:28px;padding-left:14px}
  .timetable thead th:last-child{text-align:center}
  .timetable td.time{background:var(--paper-grey)}
  .timetable td.day-alt{background:var(--blue-cell)}
  .timetable td.day{background:var(--paper)}
  .timetable tbody tr:nth-child(odd) td.day{background:#f1f1f1}
  .timetable td.sun{text-align:center}
  .timetable td.tall{line-height:1.15}
  .tt-note{position:absolute;left:56px;top:472px;font:400 14px/1 'Lato',sans-serif;color:var(--ink)}
</style>
</head>
<body>
<main class="canvas">

  <section class="card card--front" aria-label="Flyer front">
    <svg class="art" viewBox="0 0 740 522" aria-hidden="false">
      <defs>
        <linearGradient id="waveBlue" x1="0" y1="0" x2="1" y2="0">
          <stop offset="0" stop-color="#33c3ee"/><stop offset="1" stop-color="#1e88e0"/>
        </linearGradient>
        <linearGradient id="photoTone" x1="0" y1="0" x2="1" y2="1">
          <stop offset="0" stop-color="#f4f1ee"/><stop offset=".55" stop-color="#d9c7c9"/><stop offset="1" stop-color="#c9a37c"/>
        </linearGradient>
      </defs>
      <path d="M0 150 C80 135 160 140 230 170 L230 492 L0 492 Z" fill="#dcdcdc" opacity=".7"/>
      <path d="M380 0 C360 60 330 120 335 190 C342 270 420 330 470 372 C560 342 650 332 740 330 V0 Z" fill="#6c459b"/>
      <path d="M400 0 C380 60 350 120 354 188 C360 262 430 318 478 358 C565 332 650 326 740 324 V0 Z" fill="#e0e0e0"/>
      <g role="img" aria-label="Photo of a yoga teacher in a twisted side-angle pose">
        <path d="M416 0 C396 60 368 120 372 186 C378 256 440 308 486 346 C570 322 652 318 740 318 V0 Z" fill="url(#photoTone)"/>
      </g>
      <path d="M300 492 C380 420 520 372 740 350 V492 Z" fill="url(#waveBlue)"/>
      <path d="M420 422 C520 380 620 360 740 346" stroke="#6c459b" stroke-width="10" fill="none"/>
      <path d="M430 414 C525 374 625 354 740 340" stroke="#ffffff" stroke-width="4" fill="none"/>
      <circle cx="150" cy="255" r="120" fill="#33a6d7"/>
      <g role="img" aria-label="Photo of hands in prayer position holding mala beads">
        <circle cx="150" cy="255" r="110" fill="#b48fd8"/>
      </g>
      <circle cx="292" cy="305" r="82" fill="#6c459b"/>
      <circle cx="292" cy="305" r="76" fill="#ffffff"/>
      <g role="img" aria-label="Photo of a woman in a seated forward fold on a mat">
        <circle cx="292" cy="305" r="72" fill="#c8b48f"/>
      </g>
      <circle cx="400" cy="404" r="76" fill="#6c459b"/>
      <circle cx="400" cy="404" r="70" fill="#ffffff"/>
      <g role="img" aria-label="Photo of a yoga class resting in child's pose">
        <circle cx="400" cy="404" r="66" fill="#8f7a62"/>
      </g>
    </svg>

    <div class="wordmark">cedar pose loft</div>

    <ul class="contact">
      <li><svg viewBox="0 0 12 12"><circle cx="6" cy="6" r="6" fill="#33a6d7"/><path d="M6 2.5a2.2 2.2 0 0 0-2.2 2.2C3.8 6.4 6 9.5 6 9.5s2.2-3.1 2.2-4.8A2.2 2.2 0 0 0 6 2.5z" fill="#fff"/></svg>3/17 Weltmore Street, Parvindale</li>
      <li><svg viewBox="0 0 12 12"><circle cx="6" cy="6" r="6" fill="#33a6d7"/><circle cx="6" cy="6" r="3.3" fill="none" stroke="#fff" stroke-width="1"/><path d="M2.7 6h6.6M6 2.7v6.6" stroke="#fff" stroke-width="1"/></svg>cedarpose.com.au</li>
      <li><svg viewBox="0 0 12 12"><circle cx="6" cy="6" r="6" fill="#33a6d7"/><path d="M4 3l1.2 1.3-.6.9c.4.9 1 1.5 1.9 1.9l.9-.6L8.7 7.7 8 8.9C5.6 8.7 3.3 6.4 3.1 4z" fill="#fff"/></svg>Call: 0471 592 640</li>
    </ul>

    <h1 class="studio-name"><span class="main">Cedar Pose</span><span class="sub">Loft</span></h1>
    <div class="band"></div>
  </section>

  <section class="card card--back" aria-label="Flyer back">
    <h2 class="tt-title">Cedar Pose Time Table</h2>
    <div class="tt-frame"><div class="tt-inner">
      <table class="timetable">
        <colgroup>
          <col style="width:69px"><col style="width:91px"><col style="width:96px"><col style="width:90px"><col style="width:90px"><col style="width:71px"><col style="width:92px"><col>
        </colgroup>
        <thead>
          <tr><th></th><th>MON</th><th>TUE</th><th>WED</th><th>THU</th><th>FRI</th><th>SAT</th><th>SUN</th></tr>
        </thead>
        <tbody>
          <tr><td class="time">545am</td><td class="day-alt"></td><td class="day">Rise + shine*</td><td class="day-alt"></td><td class="day">Rise + shine*</td><td class="day-alt"></td><td class="day"></td><td class="day-alt sun"></td></tr>
          <tr><td class="time">900am</td><td class="day-alt"></td><td class="day"></td><td class="day-alt"></td><td class="day"></td><td class="day-alt"></td><td class="day">Vinyasa flow</td><td class="day-alt sun"></td></tr>
          <tr><td class="time">915am</td><td class="day-alt"></td><td class="day">Vinyasa flow</td><td class="day-alt"></td><td class="day"></td><td class="day-alt"></td><td class="day"></td><td class="day-alt sun">Yin</td></tr>
          <tr><td class="time">930am</td><td class="day-alt">Slow flow</td><td class="day"></td><td class="day-alt"></td><td class="day">Vinyasa flow</td><td class="day-alt"></td><td class="day"></td><td class="day-alt sun"></td></tr>
          <tr><td class="time">1030am</td><td class="day-alt"></td><td class="day"></td><td class="day-alt"></td><td class="day"></td><td class="day-alt"></td><td class="day">Pregnancy</td><td class="day-alt sun"></td></tr>
          <tr><td class="time">11am</td><td class="day-alt"></td><td class="day">Mum + baby*</td><td class="day-alt"></td><td class="day">Mum + baby*</td><td class="day-alt"></td><td class="day"></td><td class="day-alt sun"></td></tr>
          <tr><td class="time">1227:00:00</td><td class="day-alt"></td><td class="day"></td><td class="day-alt"></td><td class="day">Pregnancy</td><td class="day-alt"></td><td class="day"></td><td class="day-alt sun"></td></tr>
          <tr><td class="time">4pm</td><td class="day-alt"></td><td class="day"></td><td class="day-alt">Kids 8-12*</td><td class="day">Kids 5- 7*</td><td class="day-alt"></td><td class="day">Vinyasa flow</td><td class="day-alt sun"></td></tr>
          <tr><td class="time">445pm</td><td class="day-alt"></td><td class="day"></td><td class="day-alt">Teens 12-16*</td><td class="day"></td><td class="day-alt"></td><td class="day"></td><td class="day-alt sun"></td></tr>
          <tr><td class="time">500pm</td><td class="day-alt"></td><td class="day"></td><td class="day-alt"></td><td class="day">Teens 12-16*</td><td class="day-alt"></td><td class="day"></td><td class="day-alt sun"></td></tr>
          <tr><td class="time">600pm</td><td class="day-alt">Pregnancy</td><td class="day">Vinyasa flow</td><td class="day-alt">Slow flow</td><td class="day"></td><td class="day-alt tall">Flow +<br>Restore</td><td class="day"></td><td class="day-alt sun"></td></tr>
          <tr><td class="time">615pm</td><td class="day-alt"></td><td class="day"></td><td class="day-alt"></td><td class="day">Pregnancy</td><td class="day-alt"></td><td class="day"></td><td class="day-alt sun"></td></tr>
          <tr><td class="time" style="height:36px">730pm</td><td class="day-alt">Vinyasa flow</td><td class="day">Pregnancy</td><td class="day-alt">Yin + restore</td><td class="day tall">Women's<br>wellness*</td><td class="day-alt"></td><td class="day"></td><td class="day-alt sun"></td></tr>
        </tbody>
      </table>
    </div></div>
    <p class="tt-note">* bookings essential</p>
    <div class="band"></div>
  </section>

</main>
</body>
</html>
```